BUSINESS book cover

Publishing a book for a specific industry and hope to customize it for different industries in the future. So, design needs to be flexible. I want BRIGHT (possibly orange) cover with large words for title...really do not need illustration. Just the subtitle will change for future editions. Book is going to be 5.25" x 8"

Sorry for any confusion. The title of the book is: "Once You Reach a Yes..." The subtitle is: A Comprehensive Member Expderience Guide for Today's Club Management Professional

```html
<!DOCTYPE html>
<html lang="en">
<head>
<meta charset="utf-8">
<title>Once You Reach a Yes... — Book Cover</title>
<link href="https://fonts.googleapis.com/css2?family=Cinzel:wght@500;600;700&display=swap" rel="stylesheet">
<style>
  :root {
    --cover-red: #7b0303;
    --cover-red-deep: #650000;
    --gold-light: #fff4b0;
    --gold-mid: #e8b52a;
    --gold-deep: #9a6a08;
    --rule-gold: #f2a81c;
  }
  html, body {
    margin: 0;
    padding: 0;
    width: 827px;
    height: 1200px;
    overflow: hidden;
    background: var(--cover-red);
  }
  .cover {
    position: relative;
    width: 827px;
    height: 1200px;
    overflow: hidden;
    background: radial-gradient(ellipse at 50% 45%, var(--cover-red) 60%, var(--cover-red-deep) 100%);
    font-family: 'Cinzel', 'Times New Roman', serif;
    text-align: center;
  }
  .gold-text {
    background: linear-gradient(180deg, var(--gold-light) 0%, var(--gold-mid) 40%, var(--gold-deep) 62%, var(--gold-mid) 80%, var(--gold-light) 100%);
    -webkit-background-clip: text;
    background-clip: text;
    color: transparent;
    filter: drop-shadow(2px 3px 2px rgba(40, 0, 0, 0.55));
  }
  .author {
    position: absolute;
    top: 55px;
    left: 0;
    right: 0;
    margin: 0;
    font-size: 56px;
    font-weight: 600;
    letter-spacing: 2px;
    line-height: 70px;
  }
  .rule {
    position: absolute;
    left: 60px;
    width: 707px;
    height: 4px;
    background: linear-gradient(90deg, rgba(242,168,28,0) 0%, var(--rule-gold) 18%, #ffd25a 50%, var(--rule-gold) 82%, rgba(242,168,28,0) 100%);
  }
  .rule-top { top: 151px; }
  .rule-bottom { top: 1001px; }
  .title {
    margin: 0;
    font-weight: 600;
  }
  .title-line {
    position: absolute;
    left: 0;
    right: 0;
    font-size: 182px;
    line-height: 182px;
    letter-spacing: 1px;
  }
  .line-1 { top: 222px; }
  .line-2 { top: 390px; }
  .line-3 { top: 562px; }
  .line-4 { top: 755px; }
  .subtitle {
    position: absolute;
    top: 1040px;
    left: 40px;
    right: 40px;
    margin: 0;
    font-size: 32px;
    font-weight: 600;
    line-height: 40px;
    letter-spacing: 0.5px;
    color: #f6d36a;
  }
</style>
</head>
<body>
  <main class="cover">
    <p class="author gold-text">Dana Whitfield</p>
    <div class="rule rule-top"></div>
    <h1 class="title">
      <span class="title-line line-1 gold-text">Once</span>
      <span class="title-line line-2 gold-text">You</span>
      <span class="title-line line-3 gold-text">Reach</span>
      <span class="title-line line-4 gold-text">a Yes...</span>
    </h1>
    <div class="rule rule-bottom"></div>
    <p class="subtitle gold-text">A Comprehensive Member Experience<br>Guide for Today's Club Management<br>Professional</p>
  </main>
</body>
</html>
```